Bright Harbor Realty

We need a good looking flyer for our real estate company to impress people who are considering to sell their homes for as low as 1.5% listing commission. Please see flyer examples for reference.
555-318-4096
Real Estate

```html
<!DOCTYPE html>
<html lang="en">
<head>
<meta charset="utf-8">
<title>Bright Harbor Realty – Just Sold Flyer</title>
<link href="https://fonts.googleapis.com/css2?family=Roboto+Condensed:ital,wght@0,400;0,700;1,400;1,700;1,900&display=swap" rel="stylesheet">
<style>
  :root {
    --stage: #e4e5e6;
    --paper: #fbfbfb;
    --ink: #1c1c1c;
    --brand-blue: #0d4fa8;
    --sold-red: #e0141b;
    --rule: #2a2a2a;
    --grass: #5e9a3a;
    --sky: #8fbde6;
  }
  html, body {
    margin: 0;
    width: 1200px;
    height: 1200px;
    overflow: hidden;
    background: var(--stage);
    font-family: "Roboto Condensed", "Arial Narrow", sans-serif;
    color: var(--ink);
  }
  .flyer {
    position: absolute;
    left: 186px;
    top: 20px;
    width: 828px;
    height: 1160px;
    background: var(--paper);
    overflow: hidden;
    box-shadow: 0 4px 18px rgba(0,0,0,.18);
  }
  .brand {
    position: absolute;
    left: 34px;
    top: 32px;
    width: 160px;
    height: 160px;
    display: flex;
    flex-direction: column;
    align-items: center;
    justify-content: center;
    gap: 10px;
  }
  .brand-mark {
    width: 46px;
    height: 46px;
    background: var(--brand-blue);
  }
  .brand-name {
    font-weight: 700;
    font-size: 22px;
    color: var(--brand-blue);
    text-align: center;
    line-height: 1.05;
  }
  .offer {
    position: absolute;
    right: 37px;
    top: 30px;
    text-align: right;
    font-style: italic;
    line-height: 1;
  }
  .offer-line { font-size: 26px; margin-bottom: 6px; }
  .offer-line strong { color: var(--brand-blue); font-weight: 700; }
  .offer-line.bold { font-weight: 700; }
  .offer-call { font-size: 17px; margin-top: 2px; }
  .offer-phone {
    font-size: 37px;
    font-weight: 900;
    color: var(--brand-blue);
    margin-top: 4px;
  }
  .headline {
    position: absolute;
    left: 0;
    right: 0;
    top: 176px;
    display: flex;
    align-items: center;
    justify-content: center;
    gap: 10px;
  }
  .headline-rule { width: 86px; height: 3px; background: var(--rule); }
  .headline-text {
    font-size: 62px;
    font-weight: 900;
    font-style: italic;
    color: var(--sold-red);
    letter-spacing: -1px;
    line-height: 1;
  }
  .listing { position: absolute; width: 340px; }
  .listing-photo {
    width: 340px;
    height: 238px;
    box-sizing: border-box;
    border: 4px solid var(--brand-blue);
    border-radius: 14px;
    background: linear-gradient(to bottom, var(--sky) 0%, #d7e6f2 42%, #b9a98f 52%, #8a9a74 66%, var(--grass) 100%);
  }
  .listing-photo.townhome {
    background: linear-gradient(to bottom, #7fb0e0 0%, #dce9f4 30%, #c9a688 45%, #b48f74 68%, #c9c9c4 82%, #bdbdb8 100%);
  }
  .listing-caption {
    margin-top: 12px;
    text-align: center;
    font-weight: 700;
    font-style: italic;
    font-size: 15px;
    line-height: 1.3;
  }
  .listing-caption .price { color: var(--sold-red); }
  .l1 { left: 49px; top: 252px; }
  .l2 { left: 437px; top: 252px; }
  .l3 { left: 49px; top: 545px; }
  .l4 { left: 437px; top: 545px; }
  .l5 { left: 444px; top: 838px; }
  .savings {
    position: absolute;
    left: 36px;
    top: 836px;
    width: 356px;
  }
  .savings-title {
    font-size: 28px;
    font-weight: 700;
    color: var(--sold-red);
    margin: 0 0 4px;
    line-height: 1.1;
  }
  .savings-body {
    font-size: 14.6px;
    line-height: 1.3;
    margin: 0;
    text-align: justify;
  }
  .savings-call { font-size: 14.6px; font-weight: 700; margin: 8px 0 0; }
  .savings-phone {
    font-size: 31px;
    font-weight: 700;
    color: var(--brand-blue);
    margin: 0;
    line-height: 1.1;
  }
  .agent {
    position: absolute;
    left: 48px;
    top: 985px;
    width: 180px;
    height: 180px;
  }
  .agent svg { display: block; }
</style>
</head>
<body>
  <main class="flyer">
    <div class="brand">
      <div class="brand-mark"></div>
      <div class="brand-name">Bright Harbor Realty</div>
    </div>

    <div class="offer">
      <div class="offer-line">List for <strong>1.5% Commission,</strong></div>
      <div class="offer-line bold">Still Receive Top Marketing!</div>
      <div class="offer-call">Call Us Today and Save Thousands!</div>
      <div class="offer-phone">(555) 318 - 4096</div>
    </div>

    <div class="headline">
      <span class="headline-rule"></span>
      <span class="headline-text">JUST SOLD</span>
      <span class="headline-rule"></span>
    </div>

    <article class="listing l1">
      <div class="listing-photo" role="img" aria-label="Photo of a green single-story home with a white garage door and driveway"></div>
      <div class="listing-caption">1 1820 Seabreeze Circle<br>Wellington, FL 33414 - <span class="price">$250,000</span></div>
    </article>

    <article class="listing l2">
      <div class="listing-photo" role="img" aria-label="Photo of a gray stone-front ranch home with a wide green lawn"></div>
      <div class="listing-caption">1742 2 E Meadowlark Drive<br>Loxahatchee, FL 33470 - <span class="price">$280,000</span></div>
    </article>

    <article class="listing l3">
      <div class="listing-photo" role="img" aria-label="Photo of a light blue single-story home with palm trees and a driveway"></div>
      <div class="listing-caption">14085 Palmetto Circle<br>Wellington, FL 33414 - <span class="price">$335,000</span></div>
    </article>

    <article class="listing l4">
      <div class="listing-photo townhome" role="img" aria-label="Photo of two-story tan townhomes with parked cars and pine trees"></div>
      <div class="listing-caption">2178 Harborview Circle E<br>Deerfield Beach, FL 33442 - <span class="price">$229,500</span></div>
    </article>

    <section class="savings">
      <h2 class="savings-title">Did You Know?</h2>
      <p class="savings-body">On average, our customers save <strong>$8,750</strong> when they choose us... and they still receive top marketing, service and representation!</p>
      <p class="savings-call">Call Us Today and Save Thousands!</p>
      <p class="savings-phone">(555) 318 -4096</p>
    </section>

    <article class="listing l5">
      <div class="listing-photo townhome" role="img" aria-label="Photo of two-story tan townhomes with a paved parking area"></div>
      <div class="listing-caption">624 6 Fairway Lane Drive<br>Atlantis, FL 33462 - <span class="price">$550,000</span></div>
    </article>

    <div class="agent">
      <svg width="180" height="180" viewBox="0 0 180 180" role="img" aria-label="Portrait of the listing agent in a dark suit">
        <defs>
          <linearGradient id="agentTone" x1="0" y1="0" x2="0" y2="1">
            <stop offset="0" stop-color="#d9d9d9"/>
            <stop offset="0.55" stop-color="#9a9a9a"/>
            <stop offset="1" stop-color="#2b2b2b"/>
          </linearGradient>
        </defs>
        <circle cx="90" cy="92" r="84" fill="url(#agentTone)"/>
        <path d="M18 45 A84 84 0 0 1 162 45" fill="none" stroke="#0d4fa8" stroke-width="4"/>
        <path d="M4 100 A86 86 0 0 0 176 100" fill="none" stroke="#dcdcdc" stroke-width="3"/>
      </svg>
    </div>
  </main>
</body>
</html>
```